quillfernPRESS is launching 2 new eBooks and needs beautiful and compelling cover designs and a desig

We are launching 2 non-fiction eBooks that are part of a series but will be launched separately, so we would like to see some continuity between the 2 designs - but each should have a strong stand alone identity.

The eBooks are both in the naturopathic/holistic health niche.

ebook 1 title is:
Shaping A Thriving Clinic
(sub) The Holistic Guide to building your own successful natural and
alternative therapy business.

The book is a comprehensive guide for naturopaths and other alternative health providers - ( Naturopath,
Nutritionist, Homeopath, Acupuncturist, Chiropractor,
Massage Therapist, or Holistic Health Specialist), who are seeking to setup their own, profitable naturopathic business.

ebook 2 title is:
Silver Pathways (subtitle) Get 30 + Clients in Under a Month

(sub/sub)32 ways to market your natural and alternative therapy business

This book is a list of 32 tips for the same audience to increase there customer referrals (and therefore income).

Each book should feature
written by Carla Whitmore
published by Whitmore Publishing

Each book should feature the authors photograph on the cover (attached) - no caveats on cropping etc - whatever fits with the design.

You can see more about the writer on her website here:

http://www.lakemeadowwellness.example.au/

What we require:

1) cover art for both eBooks that conforms to Kindle and iPad specs
2) Flat & 3D book cover art for use on website and marketing campaigns
3) we will require layered PSD files on completion of project.

I'd like to add that we are seeking to build a relationship with the designer we choose for this project, as we are publishing many other titles throughout 2014

Many eBook writers jump straight to Gigly for a cover. The result is most self published books have the same generic look the 'gigly' look.

I don't want that look.

We want to reward great design and ensure quillfernPRESS eBook titles have a great look.

The winning designer will be working with us on many more projects.

Martin Oakes
quillfernPRESS

```html
<!DOCTYPE html>
<html lang="en">
<head>
<meta charset="utf-8">
<title>Shaping A Thriving Clinic — Cover</title>
<link rel="stylesheet" href="https://fonts.googleapis.com/css2?family=Russo+One&display=swap">
<style>
  :root {
    --page: #f3f2f1;
    --ink: #141012;
    --cream: #f7ecd8;
    --blush: #f4cfc6;
    --rose: #e07a86;
    --coral: #d9504c;
    --magenta: #c2307f;
    --plum: #8f2a5e;
    --spine: #e01f77;
  }
  html, body {
    margin: 0;
    padding: 0;
    overflow: hidden;
    background: var(--page);
  }
  .canvas {
    position: relative;
    width: 886px;
    height: 1200px;
    overflow: hidden;
    background: var(--page);
  }
  .cover {
    position: absolute;
    left: 133px;
    top: 40px;
    width: 620px;
    height: 1120px;
    overflow: hidden;
    font-family: "Russo One", "Arial Black", sans-serif;
    color: var(--cream);
  }
  .cover-artwork {
    position: absolute;
    inset: 0;
    background:
      radial-gradient(ellipse 55% 45% at 50% 48%, var(--cream) 0%, var(--blush) 28%, rgba(224,122,134,0.85) 55%, rgba(194,48,127,0) 80%),
      linear-gradient(160deg, var(--coral) 0%, var(--rose) 30%, var(--magenta) 60%, var(--plum) 85%, var(--coral) 100%);
  }
  .title-block {
    position: absolute;
    left: 16px;
    right: 16px;
    top: 360px;
    display: flex;
    flex-direction: column;
    align-items: flex-start;
  }
  .title-line {
    display: inline-block;
    background: var(--ink);
    font-size: 62px;
    line-height: 1;
    padding: 8px 12px 4px;
    border-radius: 6px;
    text-transform: uppercase;
    white-space: nowrap;
  }
  .title-line--second {
    margin-top: -2px;
  }
  .subtitle {
    display: inline-block;
    background: var(--ink);
    margin-top: -2px;
    padding: 8px 12px 10px;
    border-radius: 6px;
    font-size: 17.5px;
    line-height: 1.25;
    text-transform: uppercase;
    max-width: 588px;
  }
  .credits {
    position: absolute;
    left: 0;
    right: 0;
    top: 900px;
    text-align: center;
  }
  .credits-box {
    display: inline-block;
    background: var(--ink);
    padding: 10px 16px 8px;
    border-radius: 6px;
    font-size: 21px;
    line-height: 1.3;
    text-transform: uppercase;
    text-align: left;
  }
</style>
</head>
<body>
  <div class="canvas">
    <section class="cover">
      <div class="cover-artwork" role="img" aria-label="Radiating burst of hand-drawn lines in pink, red, magenta and cream streaming outward from the centre"></div>

      <div class="title-block">
        <h1 class="title-line">Shaping A</h1>
        <span class="title-line title-line--second">Thriving Clinic</span>
        <p class="subtitle">The holistic guide to building your own successful natural and alternative therapy business.</p>
      </div>

      <div class="credits">
        <div class="credits-box">
          Written by Carla Whitmore<br>
          Published by Whitmore Publishing
        </div>
      </div>
    </section>
  </div>
</body>
</html>
```